Fun, Clean Business Card For Family Focused Travel Agency

I need a business card using specific colors and fonts as in the uploaded files. Ideally, I would like a large image of the logo on the back and all the contact info on the front. Maybe the stars/dots somewhere in a flowy form.

I do want it the contact information to be clear and easy to read. I don't want it to look too busy. Maybe even a bit minimalist.

I plan or ordering the ROUNDED CORNER business cards from Cardloom, so please consider that in your design.

Target Market(s)

Families with children, couples, groups of friends

Contact Information for Business Card

Marisol Trent, Owner
Marisol@BreezeTrips.example
Cell Phone Number 555-218-4637
Office Phone Number 555-762-1094
Specializing in Fablewood destinations, Grandvista Lakeside Park, Cruises and All-Inclusive Vacations.

Nice but not required:
www.BreezeTrips.example
Facebook, Instagram, Twitter icons with username: BreezeTrips

Font styles to use
Sans Serif

Requirements
Must have
• Please try to use the colors from the logo as much as possible. I understand lighter shades/colors may be needed for some things.
Should not have
• NO SERIF FONTS. That is really the only thing I do not want at all

```html
<!DOCTYPE html>
<html lang="en">
<head>
<meta charset="utf-8">
<title>Breeze Trips – Business Card</title>
<link rel="stylesheet" href="https://fonts.googleapis.com/css2?family=Oswald:wght@500&family=Work+Sans:wght@400;500&display=swap">
<style>
  :root {
    --stage: #1f1f21;
    --card-navy: #141a33;
    --card-navy-deep: #10152b;
    --accent-orange: #f07f22;
    --silver: #c8cbd2;
    --text-light: #e9eaee;
    --muted-blue: #2a3150;
  }
  * { box-sizing: border-box; margin: 0; padding: 0; }
  html, body { width: 1200px; height: 900px; overflow: hidden; }
  body {
    background: var(--stage);
    font-family: "Work Sans", Arial, sans-serif;
    display: flex;
    flex-direction: column;
    align-items: center;
    justify-content: center;
    gap: 24px;
  }
  .card {
    width: 700px;
    height: 400px;
    border-radius: 22px;
    background: linear-gradient(160deg, var(--card-navy) 0%, var(--card-navy-deep) 100%);
    position: relative;
    color: var(--text-light);
    overflow: hidden;
  }

  /* Logo side */
  .card--brand {
    display: flex;
    flex-direction: column;
    align-items: center;
    justify-content: center;
    padding: 0 48px;
  }
  .brand-lockup {
    display: flex;
    align-items: center;
    gap: 18px;
    margin-bottom: 44px;
  }
  .brand-dot {
    width: 74px; height: 74px;
    border-radius: 50%;
    background: var(--muted-blue);
  }
  .brand-name {
    font-weight: 500;
    font-size: 58px;
    letter-spacing: 1px;
    color: var(--silver);
  }
  .brand-tagline {
    font-size: 17px;
    line-height: 1.45;
    letter-spacing: 0.6px;
    text-align: center;
    color: var(--text-light);
  }

  /* Contact side */
  .contact-main {
    position: absolute;
    top: 132px;
    left: 48px;
    right: 48px;
    display: flex;
    justify-content: center;
    align-items: center;
  }
  .identity {
    text-align: right;
    padding-right: 22px;
    white-space: nowrap;
  }
  .identity__name {
    font-family: "Oswald", "Arial Narrow", sans-serif;
    font-weight: 500;
    font-size: 36px;
    letter-spacing: 1.5px;
    color: var(--accent-orange);
    line-height: 1;
  }
  .identity__role {
    font-size: 17px;
    letter-spacing: 1px;
    margin-top: 6px;
  }
  .divider {
    width: 2px;
    height: 92px;
    background: var(--accent-orange);
    flex: none;
  }
  .contact-list {
    list-style: none;
    padding-left: 22px;
    font-size: 16px;
    letter-spacing: 0.5px;
    line-height: 1.45;
    white-space: nowrap;
  }
  .contact-list li { display: flex; align-items: center; gap: 10px; }
  .contact-list svg { width: 12px; height: 12px; flex: none; }
  .social {
    position: absolute;
    bottom: 48px;
    left: 0; right: 0;
    display: flex;
    justify-content: center;
    align-items: center;
    gap: 16px;
    font-size: 19px;
    letter-spacing: 0.8px;
  }
  .social__mark {
    width: 24px; height: 24px;
    border-radius: 4px;
    background: var(--accent-orange);
  }
</style>
</head>
<body>

  <section class="card card--brand" aria-label="Card front">
    <div class="brand-lockup">
      <span class="brand-dot" aria-hidden="true"></span>
      <span class="brand-name">Breeze Trips</span>
    </div>
    <p class="brand-tagline">Specializing in Fablewood destinations, Grandvista Lakeside Park,<br>Cruises and All-Inclusive Vacations.</p>
  </section>

  <section class="card card--contact" aria-label="Card back">
    <div class="contact-main">
      <div class="identity">
        <h1 class="identity__name">MARISOL TRENT</h1>
        <p class="identity__role">Owner</p>
      </div>
      <span class="divider" aria-hidden="true"></span>
      <ul class="contact-list">
        <li>
          <svg viewBox="0 0 12 12" aria-hidden="true"><rect x="3" y="0.8" width="6" height="10.4" rx="1.2" fill="none" stroke="var(--accent-orange)" stroke-width="1.3"/></svg>
          555-218-4637
        </li>
        <li>
          <svg viewBox="0 0 12 12" aria-hidden="true"><path d="M3 1 L5 3.5 L4 5 Q5 7.5 7 8 L8.5 7 L11 9 L9.5 11 Q3 10.5 1 2.5 Z" fill="var(--accent-orange)"/></svg>
          555-762-1094
        </li>
        <li>
          <svg viewBox="0 0 12 12" aria-hidden="true"><rect x="0.8" y="2.3" width="10.4" height="7.4" fill="none" stroke="var(--accent-orange)" stroke-width="1.2"/><path d="M1 2.8 L6 6.6 L11 2.8" fill="none" stroke="var(--accent-orange)" stroke-width="1.2"/></svg>
          Marisol@BreezeTrips.example
        </li>
        <li>
          <svg viewBox="0 0 12 12" aria-hidden="true"><circle cx="6" cy="6" r="5" fill="none" stroke="var(--accent-orange)" stroke-width="1.1"/><ellipse cx="6" cy="6" rx="2.2" ry="5" fill="none" stroke="var(--accent-orange)" stroke-width="1"/><path d="M1 6 H11" stroke="var(--accent-orange)" stroke-width="1"/></svg>
          www.BreezeTrips.example
        </li>
      </ul>
    </div>
    <div class="social">
      <span class="social__handle">BreezeTrips</span>
      <span class="social__mark" aria-hidden="true"></span>
    </div>
  </section>

</body>
</html>
```